Images Needed for Training Document

We are a staffing company that is working to help develop our leadership team. We have created a training document to help this team navigate quarterly review meetings, but need help with creating graphics/images to go with the text of the document. I am attaching the training document, with bold red notes where we need images/graphics.

If needed, I can also send a list of the exact type of images/graphics we are looking to add.

I am also attaching documents we use in other areas of the business, just to give an idea of what we typically have in our marketing.

```html
<!DOCTYPE html>
<html lang="en">
<head>
<meta charset="utf-8">
<title>Quarterly Review Meeting</title>
<link href="https://fonts.googleapis.com/css2?family=Arimo:wght@400;700&display=swap" rel="stylesheet">
<style>
  :root {
    --paper: #ffffff;
    --ink: #1a1a1a;
    --page-rule: #4a6fa5;
    --navy: #1b2f55;
    --cycle-blue: #2f7fd3;
    --flow-green: #3ba673;
    --label-navy: #1f3356;
  }
  * { margin: 0; padding: 0; box-sizing: border-box; }
  html, body { width: 929px; height: 1200px; overflow: hidden; background: var(--paper); }
  body { position: relative; font-family: "Arimo", Arial, sans-serif; color: var(--ink); }

  .page-frame {
    position: absolute; left: 2px; top: 2px; width: 925px; height: 1196px;
    border: 1.5px solid var(--page-rule);
  }
  .doc-title {
    position: absolute; top: 108px; left: 0; width: 929px; text-align: center;
    font-size: 18px; font-weight: 700; text-decoration: underline;
  }
  .block {
    position: absolute; left: 112px; width: 706px;
    font-size: 16px; line-height: 22.4px; text-align: justify;
  }
  .heading { font-weight: 700; text-align: left; }

  .intro { top: 175px; }
  .objective-head { top: 328px; }
  .objective-body { top: 357px; }
  .role-head { top: 415px; }
  .role-body { top: 441px; }

  .flow-art { position: absolute; left: 0; top: 0; width: 929px; height: 1200px; }

  .flow-box {
    position: absolute; top: 723px; height: 51px;
    display: flex; align-items: center; justify-content: center;
    color: #fff; font-weight: 700; font-size: 16px; letter-spacing: 0.3px;
  }
  .flow-box.evaluations { left: 113px; width: 147px; background: var(--navy); }
  .flow-box.execution { left: 525px; width: 318px; background: var(--flow-green); border-radius: 2px; }

  .cycle-label {
    position: absolute; left: 315px; top: 640px; width: 160px; text-align: center;
    font-weight: 700; font-size: 16px; line-height: 25px; color: var(--label-navy);
    letter-spacing: 0.3px;
  }

  .step-head { top: 806px; }
  .step-body { top: 840px; }

  .sub-head { left: 137px; top: 982px; width: 300px; }
  .sub-head span { display: inline-block; width: 28px; }
  .sub-body { left: 165px; width: 651px; top: 1020px; }
</style>
</head>
<body>
  <div class="page-frame"></div>

  <h1 class="doc-title">Quarterly Review Meeting</h1>

  <p class="block intro">A leader's ability to conduct effective quarterly meetings significantly influences our commitment to prioritizing our internal partners. We recognize that a leader's responsibilities are often driven by the needs of their partners, making much of the role reactive. Quarterly review meetings offer a proactive opportunity to evaluate performance, establish meeting flow, and develop strategies that positively impact careers. These INDEPENDENTLY run meetings also provide a chance to correct any misguided coaching given during the quarter. Let's explore the purpose, your role, and key details to ensure a successful meeting.</p>

  <p class="block heading objective-head">Objective:</p>
  <p class="block objective-body">Build trust and impact career progression through effective communication of culture, performance, and strategy with partners that are meeting baseline standards.</p>

  <p class="block heading role-head">Your Role as a Leader:</p>
  <p class="block role-body">As a leader, your role in these meetings is pivotal. You are the facilitator, the strategist, and the coach. It is your responsibility to accurately evaluate your partner, guide the conversation, ensuring that it remains focused and productive. Your leadership will set the tone for the meeting, making it a space where partners feel valued, heard, and motivated to contribute their best.</p>

  <svg class="flow-art" viewBox="0 0 929 1200" aria-hidden="true">
    <path d="M381 585 A80 80 0 1 1 326 624" fill="none" stroke="var(--cycle-blue)" stroke-width="10" stroke-linecap="round"/>
    <polyline points="399,567 379,585 399,603" fill="none" stroke="var(--cycle-blue)" stroke-width="10" stroke-linecap="round" stroke-linejoin="round"/>
    <line x1="282" y1="746" x2="500" y2="746" stroke="var(--cycle-blue)" stroke-width="8" stroke-linecap="round"/>
    <polyline points="484,730 502,746 484,762" fill="none" stroke="var(--cycle-blue)" stroke-width="8" stroke-linecap="round" stroke-linejoin="round"/>
  </svg>

  <div class="cycle-label">DETERMINE<br>MEETING FLOW</div>
  <div class="flow-box evaluations">EVALUATIONS</div>
  <div class="flow-box execution">MEETING EXECUTION &amp; FOLLOW UP</div>

  <p class="block heading step-head">Step 1:&nbsp; Evaluating Against Our Baseline Standards:</p>
  <p class="block step-body">To ensure that these meetings are productive and meaningful, it is crucial to evaluate partners against our baseline standards, as outlined in the DBO Manual. These standards should create an outline and tone for the meeting.</p>

  <p class="block heading sub-head"><span>A.</span>Attitude:</p>
  <p class="block sub-body">Attitude plays a significant role in a partner's overall performance and their impact on the team. This evaluation is subjective, but it is essential to maintain high standards. An attitude score below 7 out of 10 is considered unacceptable. Leaders should observe and assess partners' attitudes towards their work, colleagues, and the organization, noting any areas that require improvement.</p>
</body>
</html>
```